Business Card Design

I need a business card designed with a logo specific to medicine, forensic, and/or neuropathology (e.g. image of a brain). I am not particular about color but I would like something that stands out.

Target Market(s)

Individuals looking for a pathologist for primary and secondary autopsies as well as neurodegenerative work-ups.

Industry/Entity Type

Business

Contact Information for Business Card

Rosalind T. Okafor, M.D.
Board Certified Anatomic, Forensic, and Neuropathologist
412 Wrenfield Lane
Ukiah, California 95417

Requirements
Must have
• Phone number (707) 281-5034

```html
<!DOCTYPE html>
<html lang="en">
<head>
<meta charset="utf-8">
<title>Rosalind T. Okafor, M.D. — Business Card</title>
<link rel="stylesheet" href="https://fonts.googleapis.com/css2?family=Arimo:wght@400&display=swap">
<style>
  :root {
    --card: #ffffff;
    --red: #ef4f6e;
    --yellow: #fbc81a;
    --blue: #2f8fd4;
    --skin: #f2cf9c;
    --text-blue: #4ba4dc;
  }
  html, body {
    margin: 0;
    padding: 0;
    width: 1200px;
    height: 758px;
    overflow: hidden;
    background: var(--card);
  }
  .card {
    position: relative;
    width: 1200px;
    height: 758px;
    background: var(--card);
    font-family: "Arimo", Arial, sans-serif;
  }
  .icon-row {
    position: absolute;
    top: 165px;
    left: 0;
    width: 100%;
    display: flex;
    justify-content: center;
    gap: 46px;
  }
  .icon {
    width: 210px;
    height: 210px;
    display: block;
  }
  .icon-brain {
    width: 210px;
    height: 210px;
    border-radius: 50%;
    background: radial-gradient(circle at 50% 45%, var(--skin) 0 28%, var(--blue) 29%);
  }
  .details {
    position: absolute;
    top: 425px;
    left: 0;
    width: 100%;
    text-align: center;
    color: var(--text-blue);
    font-size: 26px;
    font-weight: 400;
    line-height: 44px;
    letter-spacing: 0.3px;
  }
  .details p { margin: 0; }
  .sep { padding: 0 10px; }
</style>
</head>
<body>
  <main class="card">
    <div class="icon-row">
      <svg class="icon icon-cross" viewBox="0 0 210 210" aria-label="Medical cross">
        <circle cx="105" cy="105" r="105" fill="var(--red)"/>
        <path d="M84 50h42v34h34v42h-34v34H84v-34H50V84h34z" fill="var(--card)"/>
      </svg>
      <svg class="icon icon-pill" viewBox="0 0 210 210" aria-label="Capsule pill">
        <circle cx="105" cy="105" r="105" fill="var(--yellow)"/>
        <path d="M80 75a25 25 0 0 1 50 0v30H80z" fill="var(--card)"/>
        <path d="M80 105h50v30a25 25 0 0 1-50 0z" fill="var(--red)"/>
      </svg>
      <div class="icon-brain" role="img" aria-label="Illustration of a head in profile with the brain shown"></div>
    </div>
    <section class="details">
      <p class="name">Rosalind T. Okafor, M.D.</p>
      <p class="title">Board Certified Anatomic, Forensic, and Neuropathologist</p>
      <p class="address">412 Wrenfield Lane Ukiah<span class="sep">|</span>California<span class="sep">|</span>95417</p>
      <p class="phone">(707) 281-5034</p>
    </section>
  </main>
</body>
</html>
```